Risen Lantern; The Road of the Quiet Lantern

Risen Lantern needs a banner ad design that can be used for social media campaigns and sites. RL's mission is to bring spiritual and mindfulness to veterans, first responders and survivors of trauma. We are looking for a design that represents the strength of this community (warriors) and the connection to spirituality. Also needs to include the RL logo of the tree of life (see attached).

Risen Lantern’s mission is to honor, support, and empower warriors to build the life skills needed to integrate and thrive in the world. We provide spiritual support to Veterans, First Responders, and their families through guidance, education, and advocacy.

As a veteran owned company, we know it’s impossible to explain the sacrifices required by those who serve their country. To share the wounds and scars that come from putting service before your family, friends, and yourself. To make yourself vulnerable by opening up to people who haven’t experienced what you have experienced.

Our mission is to improve the quality of life of those who have sacrificed for others by providing revolutionary spiritual services developed by and geared towards warriors.

Target Market(s)

Spiritual warriors, veterans, first responders, and survivors of trauma

Industry/Entity Type

Health And Wellness

Font styles to use
Decorative
Script

Colors
ffcf3e
ffffff

Requirements
Must have
• Main colors, Black, white, gold. Looking for something that signifies warriors. Spiritual warriors preferable. Shows strength, displine, and spiritual connection.
Nice to have
• pop of color is fine
Should not have
• Not just American soldiers, so stay away from red-white and blue

```html
<!DOCTYPE html>
<html lang="en">
<head>
<meta charset="utf-8">
<title>Risen Lantern — Spiritual and Mindfulness to Veterans</title>
<link rel="stylesheet" href="https://fonts.googleapis.com/css2?family=Cinzel:wght@500;600&display=swap">
<style>
  :root {
    --page-bg: #d2d2d2;
    --banner-black: #000000;
    --glow-white: #ffffff;
    --gold: #d2a448;
    --text-white: #ffffff;
  }
  html, body {
    margin: 0;
    padding: 0;
    width: 1200px;
    height: 1200px;
    overflow: hidden;
    background: var(--page-bg);
  }
  .canvas {
    position: relative;
    width: 1200px;
    height: 1200px;
  }
  .banner {
    position: absolute;
    left: 89px;
    top: 329px;
    width: 980px;
    height: 534px;
    display: block;
  }
  .headline {
    font-family: "Cinzel", "Times New Roman", serif;
    font-weight: 600;
    font-size: 56px;
    text-anchor: middle;
  }
  .headline-white { fill: var(--text-white); }
  .headline-gold { fill: var(--gold); }
  .brand-name {
    font-family: "Cinzel", "Times New Roman", serif;
    font-weight: 600;
    fill: var(--gold);
    text-anchor: middle;
  }
</style>
</head>
<body>
<div class="canvas">
  <svg class="banner" viewBox="0 0 980 534" xmlns="http://www.w3.org/2000/svg">
    <defs>
      <radialGradient id="light" gradientUnits="userSpaceOnUse" cx="845" cy="150" r="520"
                      gradientTransform="translate(845 150) scale(1 1.15) translate(-845 -150)">
        <stop offset="0" stop-color="#ffffff"/>
        <stop offset="0.18" stop-color="#f2f2f2"/>
        <stop offset="0.4" stop-color="#b5b5b5"/>
        <stop offset="0.62" stop-color="#4a4a4a"/>
        <stop offset="0.82" stop-color="#0d0d0d"/>
        <stop offset="1" stop-color="#000000"/>
      </radialGradient>
      <radialGradient id="figure-tone" gradientUnits="userSpaceOnUse" cx="800" cy="250" r="170"
                      gradientTransform="translate(800 250) scale(0.45 1.3) translate(-800 -250)">
        <stop offset="0" stop-color="#111111" stop-opacity="0.85"/>
        <stop offset="0.6" stop-color="#222222" stop-opacity="0.5"/>
        <stop offset="1" stop-color="#333333" stop-opacity="0"/>
      </radialGradient>
    </defs>

    <rect class="banner-bg" width="980" height="534" fill="var(--banner-black)"/>
    <rect class="banner-light" width="980" height="534" fill="url(#light)"/>

    <g class="hero-photo" role="img" aria-label="Silhouette of a soldier with a rifle walking into bright misty light">
      <rect x="680" y="20" width="240" height="480" fill="url(#figure-tone)"/>
    </g>

    <path class="gold-frame" d="M751 25 H25 V505 H751" fill="none" stroke="var(--gold)" stroke-width="1.5"/>

    <text class="headline headline-white" x="310" y="115">S<tspan font-size="44">PIRITUAL</tspan></text>
    <text class="headline headline-gold" x="313" y="173">A<tspan font-size="44">ND</tspan> M<tspan font-size="44">INDFULNESS</tspan></text>
    <text class="headline headline-white" x="311" y="232">T<tspan font-size="44">O</tspan> V<tspan font-size="44">ETERANS</tspan></text>

    <g class="brand-mark-initials">
      <circle cx="187" cy="383" r="55" fill="none" stroke="var(--gold)" stroke-width="1.5"/>
      <text class="brand-name" x="187" y="394" font-size="32">RL</text>
    </g>

    <line class="brand-divider" x1="268" y1="316" x2="268" y2="451" stroke="var(--gold)" stroke-width="1"/>

    <g class="brand-mark-name">
      <text class="brand-name" x="379" y="430" font-size="24">Risen Lantern</text>
    </g>
  </svg>
</div>
</body>
</html>
```